Summer Drinks Flyer for Coffee Shop

We are a coffee shop in London and would like to have a cool and nice flyer for our summer drinks (juices and frozen drink) flyer - see on the attached file for the list

Attached you can find an "attempt" - please note that I would no necessary need the image below.

I also attache our new logo.

thank you

Industry/Entity Type

Coffee Shop

```html
<!DOCTYPE html>
<html lang="en">
<head>
<meta charset="utf-8">
<title>Vellutina – Summer Drinks</title>
<link href="https://fonts.googleapis.com/css2?family=Handlee&display=swap" rel="stylesheet">
<style>
  :root {
    --gold: #b3955a;
    --ink: #2e2e2e;
    --berry: #c72a35;
    --leaf: #3a9c4c;
    --amber: #e0852c;
    --paper: #ffffff;
  }
  * { margin: 0; padding: 0; box-sizing: border-box; }
  html, body { width: 849px; height: 1200px; overflow: hidden; background: var(--paper); }
  .flyer {
    position: relative;
    width: 849px;
    height: 1200px;
    background: var(--paper);
    font-family: "Handlee", cursive;
    color: var(--ink);
    overflow: hidden;
  }
  .brand {
    position: absolute;
    top: 44px;
    left: 0;
    width: 100%;
    text-align: center;
    color: var(--gold);
  }
  .brand-dot {
    display: block;
    width: 40px;
    height: 40px;
    margin: 0 auto 8px;
    border-radius: 50%;
    background: var(--gold);
  }
  .brand-name { font-size: 62px; line-height: 1; letter-spacing: 2px; }
  .hero { position: absolute; top: 170px; left: 0; width: 849px; height: 580px; }
  .hero-title {
    position: absolute;
    top: 402px;
    left: 80px;
    font-size: 66px;
    color: rgba(255,255,255,0.85);
    letter-spacing: 2px;
    white-space: nowrap;
  }
  .menu-group { position: absolute; left: 54px; }
  .menu-group h2 { font-weight: 400; font-size: 34px; line-height: 1.1; }
  .menu-group ul { list-style: none; font-size: 20px; line-height: 24px; letter-spacing: 0.5px; }
  .frozen { top: 742px; }
  .frozen h2, .frozen-price { color: var(--berry); }
  .juices { top: 855px; }
  .juices h2, .juices-price { color: var(--leaf); }
  .coffees { top: 1038px; }
  .coffees h2, .coffees-price { color: var(--amber); }
  .price {
    position: absolute;
    left: 600px;
    font-size: 52px;
    line-height: 1;
    letter-spacing: 1px;
  }
  .frozen-price { top: 772px; }
  .juices-price { top: 914px; }
  .coffees-price { top: 1068px; }
  .extra {
    position: absolute;
    width: 146px;
    height: 146px;
    border-radius: 50%;
    color: #fff;
    display: flex;
    align-items: center;
    justify-content: center;
    text-align: center;
    font-size: 18px;
    line-height: 20px;
    padding: 0 28px;
  }
  .extra-mint { left: 358px; top: 868px; background: var(--leaf); }
  .extra-syrup { left: 359px; top: 1030px; background: var(--amber); }
</style>
</head>
<body>
<main class="flyer">
  <header class="brand">
    <span class="brand-dot"></span>
    <div class="brand-name">vellutina</div>
  </header>

  <svg class="hero" viewBox="0 0 849 580" role="img" aria-label="Photo of rows of glasses filled with red, green and yellow summer fruit drinks">
    <defs>
      <linearGradient id="drinkTones" x1="0" y1="0" x2="1" y2="0">
        <stop offset="0" stop-color="#c9483e"/>
        <stop offset="0.25" stop-color="#9fbf57"/>
        <stop offset="0.55" stop-color="#e3b24a"/>
        <stop offset="0.8" stop-color="#a9c55c"/>
        <stop offset="1" stop-color="#c75a45"/>
      </linearGradient>
      <linearGradient id="glassShade" x1="0" y1="0" x2="0" y2="1">
        <stop offset="0" stop-color="#e9e4de" stop-opacity="0.9"/>
        <stop offset="0.35" stop-color="#ffffff" stop-opacity="0.15"/>
        <stop offset="1" stop-color="#5a4a2a" stop-opacity="0.2"/>
      </linearGradient>
      <clipPath id="heroShape">
        <path d="M0 82 Q 420 -10 849 12 L849 495 C 600 470 330 520 0 565 Z"/>
      </clipPath>
    </defs>
    <g clip-path="url(#heroShape)">
      <rect width="849" height="580" fill="url(#drinkTones)"/>
      <rect width="849" height="580" fill="url(#glassShade)"/>
    </g>
    <path d="M0 82 Q 420 -10 849 12" fill="none" stroke="var(--gold)" stroke-width="7"/>
  </svg>

  <div class="hero-title">It’s summer again</div>

  <section class="menu-group frozen">
    <h2>Frozen Fruit Drinks</h2>
    <ul>
      <li>Strawberry and banana</li>
      <li>Pineapple, mango and banana</li>
    </ul>
  </section>
  <div class="price frozen-price">£2·95</div>

  <section class="menu-group juices">
    <h2>Fruit Juices</h2>
    <ul>
      <li>Orange and carrot</li>
      <li>Orange and pineapple</li>
      <li>Pineapple and apple</li>
      <li>Apple and kiwi</li>
      <li>Carrot and ginger</li>
    </ul>
  </section>
  <div class="extra extra-mint">add mint or ginger for free</div>
  <div class="price juices-price">£2·95</div>

  <section class="menu-group coffees">
    <h2>Iced-Coffees</h2>
    <ul>
      <li>Iced Coffee</li>
      <li>Iced Latte</li>
      <li>Iced Chocolate Drink</li>
    </ul>
  </section>
  <div class="extra extra-syrup">add syrup shot for 10p</div>
  <div class="price coffees-price">£2·95</div>
</main>
</body>
</html>
```